Cove Ridge Cardiac

Business cards for cardiology practice. eventually we will add picture (head shot) but for now just go with full color cards. Will need to use same template and design for three other providers with minor change in the designation besides name.
Looking for a design where logo stands out so as the name.
Industry/Entity Type
Business
Contact Information for Business Card
Vikram Desai, M.D.
Board Certified in Cardiovascular Disease, Interventional Cardiology & Nuclear Cardiology
812 Fernway, Suite B
Lindale, TX 77412
Telephone: (832) 617 2283
FAx: (832) 617-2284
Email: vdesai@coveridgecardiac.example
Web: www. coveridgecardiac.example
Look and feel
Each slider illustrates characteristics of the customer's brand and the style your logo design should communicate.

```html
<!DOCTYPE html>
<html lang="en">
<head>
<meta charset="utf-8">
<title>Cove Ridge Cardiac – Business Card</title>
<link href="https://fonts.googleapis.com/css2?family=Open+Sans:wght@400;600;700&display=swap" rel="stylesheet">
<style>
  :root {
    --brand-red: #c0202e;
    --ink-black: #0d0d0d;
    --card-white: #f4f4f4;
    --card-shade: #e2e2e2;
    --page-bg: #2a2a2a;
    --text-dark: #1a1a1a;
  }
  * { margin: 0; padding: 0; box-sizing: border-box; }
  html, body {
    width: 1200px; height: 900px; overflow: hidden;
    background: var(--page-bg);
    font-family: "Open Sans", Arial, sans-serif;
  }
  .business-card {
    position: absolute; left: 100px; top: 165px;
    width: 1000px; height: 570px;
    background: linear-gradient(180deg, var(--card-white) 0%, var(--card-shade) 100%);
    overflow: hidden;
    box-shadow: 0 20px 50px rgba(0,0,0,.6);
  }
  .header-band {
    position: absolute; left: 0; top: 0; width: 100%; height: 150px;
    background: var(--brand-red);
  }
  .designation-tab {
    position: absolute; right: 0; top: 42px; width: 460px; height: 86px;
  }
  .designation-text {
    position: absolute; right: 24px; top: 52px; width: 400px;
    color: #fff; font-size: 19px; line-height: 1.22; text-align: right;
  }
  .provider-name {
    position: absolute; left: 58px; top: 92px;
    color: #fff; font-size: 34px; font-weight: 700; letter-spacing: .5px;
  }
  .practice-mark {
    position: absolute; left: 80px; top: 290px;
    display: flex; align-items: center; gap: 16px;
  }
  .practice-mark .mark-dot {
    width: 26px; height: 26px; border-radius: 50%; background: var(--brand-red);
  }
  .practice-mark .mark-name {
    color: var(--ink-black); font-size: 40px; font-weight: 700;
  }
  .contact-list {
    position: absolute; left: 560px; top: 190px;
    list-style: none; font-size: 22px; line-height: 1.6; color: var(--text-dark);
  }
  .contact-list .label { color: var(--brand-red); font-weight: 700; }
  .office-address {
    position: absolute; left: 580px; top: 372px;
    font-style: normal; font-size: 22px; line-height: 1.4; color: var(--brand-red);
  }
  .office-address .office-name { color: var(--ink-black); font-weight: 700; display: block; }
  .footer-stripe {
    position: absolute; left: 0; top: 438px; width: 100%; height: 14px;
    background: var(--brand-red);
  }
  .footer-band {
    position: absolute; left: 0; top: 452px; width: 100%; height: 118px;
    background: var(--ink-black);
  }
</style>
</head>
<body>
  <div class="business-card">
    <div class="header-band"></div>
    <svg class="designation-tab" viewBox="0 0 460 86" preserveAspectRatio="none" aria-hidden="true">
      <path d="M60 0 H460 V86 H0 C30 86 30 0 60 0 Z" fill="var(--ink-black)"/>
    </svg>
    <p class="designation-text">M.D. Board Certified in Cardiovascular Disease, Interventional Cardiology &amp; Nuclear Cardiology</p>
    <h1 class="provider-name">VIKRAM DESAI</h1>

    <div class="practice-mark">
      <span class="mark-dot"></span>
      <span class="mark-name">Cove Ridge Cardiac</span>
    </div>

    <ul class="contact-list">
      <li><span class="label">Telephone:</span> (832) 617 2283</li>
      <li><span class="label">Fax:</span> (832) 617-2284</li>
      <li><span class="label">Email:</span> vdesai@coveridgecardiac.example</li>
      <li><span class="label">Website:</span> www.coveridgecardiac.example</li>
    </ul>

    <address class="office-address">
      <span class="office-name">COVE RIDGE CARDIAC</span>
      812 Fernway, Suite B<br>
      Lindale, TX 77412
    </address>

    <div class="footer-stripe"></div>
    <div class="footer-band"></div>
  </div>
</body>
</html>
```